BRELM - Letterhead

Willowmere Institute of Letters and Crafts (BRELM) is a non-profit organization that operates two tuition-free public schools - BRELM Elementary for grades K to 5th and BRELM College Prep for grades 6-12.

We are looking for a letterhead primarily to be used on Google Docs and Microsoft Word. Attached are two versions of our logo. One with our name spelled out and one with the acronym.

For Letterhead, we would like 3 addresses listed:

BRELM HQ
41872 Hollow Brook Lane, Suite 308
Fernhaven, CA 99041

BRELM Elementary (K-5)
18460 Marsh Ridge Boulevard
Fernhaven, CA 99041

BRELM College Prep (6-12)
27314 Del Sol Terrace
Cedar Hollow Bay, CA 99058

Our Phone Number is (555) 418-7062
Our Fax Number is the same (555) 418-7062

Our website is www.brelmschools.org

Target Market(s)

Education

Industry/Entity Type

Education

Font styles to use
Sans Serif

Colors
0054AA
0677BA
7BADD7
CADEEF
E8F1F8

Requirements
Must have
• Logo, Address, Phone Number, Website.
Nice to have
• Modern and clean design.
Should not have
• Prefer that there is no bleed -- the letterhead will mostly be used in PDF format however sometimes it will be printed and our printers can not do a full bleed

```html
<!DOCTYPE html>
<html lang="en">
<head>
<meta charset="utf-8">
<title>BRELM Letterhead</title>
<link href="https://fonts.googleapis.com/css2?family=Arimo:wght@400;500;700&family=Fira+Sans+Condensed:wght@600&family=Josefin+Sans:wght@300;400;600&display=swap" rel="stylesheet">
<style>
  :root {
    --backdrop: #dcdcdc;
    --paper: #ebebeb;
    --band: #173b8c;
    --brand-blue: #1b3c8f;
    --ink-dark: #1a1a1a;
    --ink-grey: #7a7a7a;
    --footer-ink: #3a3a3a;
    --rule: #555555;
    --icon-yellow: #f2b705;
    --icon-red: #e2552b;
    --icon-green: #2e9a3e;
  }
  html, body {
    margin: 0;
    padding: 0;
    width: 1074px;
    height: 1200px;
    overflow: hidden;
    background: var(--backdrop);
  }
  .letterhead {
    position: absolute;
    left: 73px;
    top: 0;
    width: 927px;
    height: 1200px;
    background: var(--paper);
    font-family: "Arimo", Arial, sans-serif;
  }
  .header-band {
    position: absolute;
    left: 0;
    top: 43px;
    width: 470px;
    height: 89px;
    background: var(--band);
    clip-path: polygon(0 0, 100% 0, 96% 100%, 0 100%);
  }
  .contact-list {
    position: absolute;
    left: 46px;
    top: 59px;
    margin: 0;
    padding: 0;
    list-style: none;
    font-family: "Josefin Sans", sans-serif;
    font-size: 15px;
    color: #ffffff;
  }
  .contact-list li {
    display: flex;
    align-items: center;
    height: 20.5px;
    letter-spacing: 0.2px;
  }
  .contact-list svg { width: 13px; height: 13px; margin-right: 11px; }
  .brand {
    position: absolute;
    left: 496px;
    top: 52px;
    display: flex;
    align-items: center;
  }
  .brand-mark {
    width: 60px;
    height: 60px;
    background: var(--brand-blue);
    margin-right: 14px;
  }
  .brand-name {
    font-family: "Fira Sans Condensed", sans-serif;
    font-weight: 600;
    font-size: 32px;
    line-height: 35px;
    letter-spacing: 0.3px;
    color: var(--brand-blue);
    white-space: nowrap;
  }
  .meta-label {
    position: absolute;
    font-size: 14.5px;
    font-weight: 700;
    color: var(--ink-dark);
  }
  .meta-value {
    display: block;
    font-weight: 400;
    color: var(--ink-grey);
    margin-top: 3px;
  }
  .subject { left: 273px; top: 305px; }
  .date { left: 763px; top: 302px; }
  .salutation {
    position: absolute;
    left: 273px;
    top: 425px;
    font-size: 19.5px;
    font-weight: 500;
    color: var(--ink-grey);
    margin: 0;
  }
  .body-copy {
    position: absolute;
    left: 273px;
    width: 568px;
    margin: 0;
    font-size: 14.9px;
    line-height: 20.4px;
    color: var(--ink-grey);
    text-align: justify;
    text-align-last: justify;
    hyphens: manual;
  }
  .para-1 { top: 469px; }
  .para-2 { top: 630px; }
  .para-3 { top: 750px; }
  .side-note {
    position: absolute;
    right: 725px;
    width: 180px;
    text-align: right;
    font-size: 14.9px;
    line-height: 20.4px;
    color: var(--ink-grey);
    margin: 0;
  }
  .side-note strong { font-weight: 400; color: var(--ink-dark); }
  .side-note-1 { top: 520px; color: #4a4a4a; }
  .side-note-2 { top: 592px; }
  .signature {
    position: absolute;
    left: 273px;
    top: 898px;
    font-size: 19.5px;
    font-weight: 500;
    line-height: 25px;
    color: var(--ink-grey);
    margin: 0;
  }
  .campus {
    position: absolute;
    top: 1103px;
    margin: 0;
    font-family: "Josefin Sans", sans-serif;
    font-weight: 300;
    font-size: 15.5px;
    line-height: 20.5px;
    color: var(--footer-ink);
    font-style: normal;
    white-space: nowrap;
  }
  .campus-name {
    display: block;
    font-weight: 600;
    color: var(--brand-blue);
  }
  .campus-hq { left: 52px; }
  .campus-elementary { left: 359px; }
  .campus-prep { left: 646px; }
  .footer-rule {
    position: absolute;
    top: 1101px;
    width: 1px;
    height: 56px;
    background: var(--rule);
  }
  .rule-1 { left: 316px; }
  .rule-2 { left: 608px; }
</style>
</head>
<body>
<main class="letterhead">
  <div class="header-band"></div>
  <ul class="contact-list">
    <li>
      <svg viewBox="0 0 13 13" aria-hidden="true"><circle cx="6.5" cy="6.5" r="6.5" fill="var(--icon-yellow)"/><path d="M4 3.5h1.5l.8 2-1 .7a5 5 0 0 0 1.7 1.7l.7-1 2 .8V9.5A1 1 0 0 1 8.7 10 6 6 0 0 1 3 4.3 1 1 0 0 1 4 3.5z" fill="#fff"/></svg>
      (555) 418-7062
    </li>
    <li>
      <svg viewBox="0 0 13 13" aria-hidden="true"><circle cx="6.5" cy="6.5" r="6.5" fill="var(--icon-red)"/><rect x="4" y="3" width="5" height="3" fill="#fff"/><rect x="3" y="6" width="7" height="4" rx="0.6" fill="#fff"/></svg>
      (555) 418-7062
    </li>
    <li>
      <svg viewBox="0 0 13 13" aria-hidden="true"><circle cx="6.5" cy="6.5" r="6.5" fill="var(--icon-green)"/><circle cx="6.5" cy="6.5" r="3.6" fill="none" stroke="#fff" stroke-width="1"/><path d="M2.9 6.5h7.2M6.5 2.9v7.2" stroke="#fff" stroke-width="0.9"/></svg>
      www.brelmschools.org
    </li>
  </ul>

  <div class="brand">
    <div class="brand-mark"></div>
    <div class="brand-name">Willowmere Institute<br>of Letters and Crafts</div>
  </div>

  <div class="meta-label subject">SUBJECT :<span class="meta-value">Lorem Ipsum is simply dummy</span></div>
  <div class="meta-label date">DATE :<span class="meta-value">15-09-2017</span></div>

  <p class="salutation">Dear Person,</p>

  <p class="side-note side-note-1">Lorem Ipsum is<br>simply dummy text<br>of the printing</p>
  <p class="side-note side-note-2"><strong>Lorem Ipsum is</strong><br>simply dummy text</p>

  <p class="body-copy para-1">Lorem Ipsum is simply dummy text of the printing and typesetting industry. Lorem Ipsum has been the industry's standard dummy text ever since the 1500s, when an unknown printer took a galley of type and scrambled it to make a type specimen book. It has survived not only five centuries, but also the leap into electronic typesetting, re&shy;maining essentially unchanged. It was popularised in the 1960s with the release of Tessaret sheets containing Lorem Ipsum passages, and more recently with desktop publishing software like Orvan PageSmith including versions of Lorem Ipsum.</p>
  <p class="body-copy para-2">Lorem Ipsum is simply dummy text of the printing and typesetting industry. Lorem Ipsum has been the industry's standard dummy text ever since the 1500s, when an unknown printer took a galley of type and scrambled it to make a type specimen book. It has survived not only five centuries, but also the leap into electronic typesetting, re&shy;maining essentially unchanged. It was popularised in the 1960s with the release of</p>
  <p class="body-copy para-3">Tessaret sheets containing Lorem Ipsum passages, and more recently with desktop publishing software like Orvan PageSmith including versions of Lorem Ipsum.lease of Tessaret sheets containing Lorem Ipsum passages, and more recently with desktop publishing software like Orvan PageSmith including versions of Lorem Ipsum. publishing software like Orvan PageSmith including versions of Lorem Ipsum.</p>

  <p class="signature">Daniel Hartwell<br>Managing Director</p>

  <address class="campus campus-hq"><span class="campus-name">BRELM HQ</span>41872 Hollow Brook Lane, Suite 308<br>Fernhaven, CA 99041</address>
  <div class="footer-rule rule-1"></div>
  <address class="campus campus-elementary"><span class="campus-name">BRELM Elementary (K-5)</span>18460 Marsh Ridge Boulevard<br>Fernhaven, CA 99041</address>
  <div class="footer-rule rule-2"></div>
  <address class="campus campus-prep"><span class="campus-name">BRELM College Prep (6-12)</span>27314 Del Sol Terrace<br>Cedar Hollow Bay, CA 99058</address>
</main>
</body>
</html>
```